Event Newsletter for Financial Advisors

Create a newsletter that only goes out to our field financial advisors.

Creating awareness around upcoming events, highlighting past events with pictures/video, and linking registrations to the newsletter.

```html
<!DOCTYPE html>
<html lang="en">
<head>
<meta charset="UTF-8">
<title>Northvale Advisor Events Newsletter</title>
<link href="https://fonts.googleapis.com/css2?family=Oswald:wght@400;500;600&family=Inter:wght@400;500;600&display=swap" rel="stylesheet">
<style>
:root{
  --brand:#d70c4e;
  --brand-dark:#c2184a;
  --ink:#111111;
  --text:#222222;
  --muted:#e6e6e6;
  --white:#ffffff;
  --footer:#000000;
  --rule:#444444;
}
*{box-sizing:border-box;margin:0;padding:0}
html,body{width:1200px;height:2724px;overflow:hidden;background:var(--white)}
body{position:relative;font-family:"Inter",sans-serif;color:var(--text)}
.abs{position:absolute}

.site-header{position:absolute;left:0;top:0;width:1200px;height:111px;display:flex;align-items:center;justify-content:center}
.brand-name{font-family:"Inter",sans-serif;font-weight:600;font-size:62px;letter-spacing:-1px;color:var(--ink);line-height:1}

.hero{position:absolute;left:0;top:111px;width:1200px;height:567px;
  background:linear-gradient(90deg,rgba(30,34,40,.75) 0%,rgba(60,68,76,.35) 35%,rgba(0,0,0,0) 55%),
  linear-gradient(100deg,#4a525a 0%,#8b959c 35%,#6e767c 55%,#3d4349 75%,#7f888e 100%)}
.hero-title{position:absolute;left:57px;top:140px;font-family:"Oswald",sans-serif;font-weight:500;font-size:84px;line-height:100px;color:var(--white)}
.btn{display:flex;align-items:center;justify-content:center;background:var(--brand);color:var(--white);font-family:"Oswald",sans-serif;font-weight:500;border-radius:3px}
.hero-cta{position:absolute;left:58px;top:357px;width:149px;height:57px;font-size:21px}

.section-title{font-family:"Oswald",sans-serif;font-weight:500;color:var(--ink);font-size:60px;line-height:1}
.events-title{position:absolute;left:60px;top:735px}

.event-row{position:absolute;left:59px;width:680px;height:140px}
.date-box{position:absolute;left:0;top:0;width:139px;height:140px;border:1.5px solid #333;text-align:center;background:var(--white)}
.date-day{font-family:"Oswald",sans-serif;font-size:24px;margin-top:8px;color:var(--ink);line-height:30px}
.date-num{font-family:"Oswald",sans-serif;font-size:46px;color:var(--brand);line-height:58px;font-weight:500}
.date-month{position:absolute;left:0;bottom:0;width:100%;height:30px;background:var(--muted);font-size:14px;line-height:30px;color:var(--ink)}
.event-info{position:absolute;left:167px;top:0;width:520px}
.event-head{font-size:18px;line-height:36px;color:var(--ink)}
.event-head strong{font-family:"Oswald",sans-serif;font-weight:400;font-size:26px}
.event-line{font-size:18px;line-height:30px;color:var(--ink);margin-top:4px}
.event-meta{display:flex;align-items:center;font-size:15px;margin-top:12px;color:var(--ink);white-space:nowrap}
.event-meta svg{flex:none}
.sep{margin:0 14px 0 16px}
.event-link{color:var(--brand);margin-left:12px}

.event-card{position:absolute;left:777px;width:363px;height:298px;background:linear-gradient(135deg,var(--brand-dark),var(--brand));color:var(--white);padding:26px 27px 0 27px;box-shadow:0 4px 10px rgba(0,0,0,.15)}
.card-top{display:flex;justify-content:space-between;align-items:baseline}
.card-name{font-family:"Oswald",sans-serif;font-size:36px;font-weight:400}
.card-date{font-size:21px}
.card-body{font-size:15px;font-weight:500;line-height:30px;text-align:justify;margin-top:14px}

.newsletter-title{position:absolute;left:0;top:1922px;width:1200px;text-align:center}
.newsletter-title .accent{color:var(--brand)}
.newsletter-copy{position:absolute;left:0;top:2022px;width:1200px;text-align:center;font-size:16.5px;line-height:30px;color:var(--ink)}
.email-input{position:absolute;left:247px;top:2119px;width:506px;height:55px;border:1.5px solid #cfcfcf;border-radius:4px;font-size:17px;color:#666;display:flex;align-items:center;padding-left:28px}
.subscribe{position:absolute;left:775px;top:2121px;width:176px;height:52px;font-size:25px;box-shadow:0 3px 8px rgba(0,0,0,.2)}

.site-footer{position:absolute;left:0;top:2260px;width:1200px;height:464px;background:var(--footer);color:var(--white)}
.footer-brand{position:absolute;left:63px;top:170px;color:var(--white);font-size:66px}
.contact-title{position:absolute;left:399px;top:70px;font-family:"Inter",sans-serif;font-weight:600;font-size:30px;letter-spacing:1px}
.contact-item{position:absolute;display:flex;align-items:center;font-size:17px;font-weight:500;line-height:39px}
.icon-dot{width:48px;height:48px;border-radius:50%;background:var(--brand);display:flex;align-items:center;justify-content:center;margin-right:24px;flex:none}
.footer-rule{position:absolute;left:59px;top:393px;width:1082px;height:1px;background:var(--rule)}
.copyright{position:absolute;left:0;top:415px;width:1200px;text-align:center;font-size:17px;font-weight:500}
</style>
</head>
<body>

<header class="site-header">
  <span class="brand-name">Northvale</span>
</header>

<section class="hero" role="img" aria-label="Photo of two advisors in business attire discussing a tablet in a modern office">
  <h1 class="hero-title">Welcome To<br>Northvale</h1>
  <a class="btn hero-cta">Register Now</a>
</section>

<h2 class="section-title events-title">Upcoming Events</h2>

<!-- event rows -->
<div class="event-row" style="top:843px">
  <div class="date-box"><div class="date-day">Wed</div><div class="date-num">04</div><div class="date-month">June 2024</div></div>
  <div class="event-info">
    <div class="event-head"><strong>Lorem ipsum dolor sit amet, consectetur :</strong> Ut enim ad</div>
    <div class="event-line">minima veniam, quis nostrum exercitationem ullam</div>
    <div class="event-meta">
      <svg width="14" height="20" viewBox="0 0 14 20"><path d="M7 0C3.1 0 0 3.1 0 7c0 5.2 7 13 7 13s7-7.8 7-13c0-3.9-3.1-7-7-7zm0 9.5A2.5 2.5 0 1 1 7 4.5a2.5 2.5 0 0 1 0 5z" fill="#111"/></svg>
      <span style="margin-left:10px">410 W. Harbor Street, Suite</span><span class="sep">|</span>
      <svg width="20" height="20" viewBox="0 0 20 20" fill="none" stroke="#d70c4e" stroke-width="1.4"><circle cx="10" cy="10" r="8.5"/><ellipse cx="10" cy="10" rx="3.8" ry="8.5"/><path d="M1.5 10h17M3 5.5h14M3 14.5h14"/></svg>
      <span class="event-link">www.northvale-events.com</span>
    </div>
  </div>
</div>
<div class="event-row" style="top:1061px">
  <div class="date-box"><div class="date-day">Wed</div><div class="date-num">04</div><div class="date-month">June 2024</div></div>
  <div class="event-info">
    <div class="event-head"><strong>Lorem ipsum dolor sit amet, consectetur :</strong> Ut enim ad</div>
    <div class="event-line">minima veniam, quis nostrum exercitationem ullam</div>
    <div class="event-meta">
      <svg width="14" height="20" viewBox="0 0 14 20"><path d="M7 0C3.1 0 0 3.1 0 7c0 5.2 7 13 7 13s7-7.8 7-13c0-3.9-3.1-7-7-7zm0 9.5A2.5 2.5 0 1 1 7 4.5a2.5 2.5 0 0 1 0 5z" fill="#111"/></svg>
      <span style="margin-left:10px">410 W. Harbor Street, Suite</span><span class="sep">|</span>
      <svg width="20" height="20" viewBox="0 0 20 20" fill="none" stroke="#d70c4e" stroke-width="1.4"><circle cx="10" cy="10" r="8.5"/><ellipse cx="10" cy="10" rx="3.8" ry="8.5"/><path d="M1.5 10h17M3 5.5h14M3 14.5h14"/></svg>
      <span class="event-link">www.northvale-events.com</span>
    </div>
  </div>
</div>
<div class="event-row" style="top:1279px">
  <div class="date-box"><div class="date-day">Wed</div><div class="date-num">04</div><div class="date-month">June 2024</div></div>
  <div class="event-info">
    <div class="event-head"><strong>Lorem ipsum dolor sit amet, consectetur :</strong> Ut enim ad</div>
    <div class="event-line">minima veniam, quis nostrum exercitationem ullam</div>
    <div class="event-meta">
      <svg width="14" height="20" viewBox="0 0 14 20"><path d="M7 0C3.1 0 0 3.1 0 7c0 5.2 7 13 7 13s7-7.8 7-13c0-3.9-3.1-7-7-7zm0 9.5A2.5 2.5 0 1 1 7 4.5a2.5 2.5 0 0 1 0 5z" fill="#111"/></svg>
      <span style="margin-left:10px">410 W. Harbor Street, Suite</span><span class="sep">|</span>
      <svg width="20" height="20" viewBox="0 0 20 20" fill="none" stroke="#d70c4e" stroke-width="1.4"><circle cx="10" cy="10" r="8.5"/><ellipse cx="10" cy="10" rx="3.8" ry="8.5"/><path d="M1.5 10h17M3 5.5h14M3 14.5h14"/></svg>
      <span class="event-link">www.northvale-events.com</span>
    </div>
  </div>
</div>
<div class="event-row" style="top:1498px">
  <div class="date-box"><div class="date-day">Wed</div><div class="date-num">04</div><div class="date-month">June 2024</div></div>
  <div class="event-info">
    <div class="event-head"><strong>Lorem ipsum dolor sit amet, consectetur :</strong> Ut enim ad</div>
    <div class="event-line">minima veniam, quis nostrum exercitationem ullam</div>
    <div class="event-meta">
      <svg width="14" height="20" viewBox="0 0 14 20"><path d="M7 0C3.1 0 0 3.1 0 7c0 5.2 7 13 7 13s7-7.8 7-13c0-3.9-3.1-7-7-7zm0 9.5A2.5 2.5 0 1 1 7 4.5a2.5 2.5 0 0 1 0 5z" fill="#111"/></svg>
      <span style="margin-left:10px">410 W. Harbor Street, Suite</span><span class="sep">|</span>
      <svg width="20" height="20" viewBox="0 0 20 20" fill="none" stroke="#d70c4e" stroke-width="1.4"><circle cx="10" cy="10" r="8.5"/><ellipse cx="10" cy="10" rx="3.8" ry="8.5"/><path d="M1.5 10h17M3 5.5h14M3 14.5h14"/></svg>
      <span class="event-link">www.northvale-events.com</span>
    </div>
  </div>
</div>
<div class="event-row" style="top:1716px">
  <div class="date-box"><div class="date-day">Wed</div><div class="date-num">04</div><div class="date-month">June 2024</div></div>
  <div class="event-info">
    <div class="event-head"><strong>Lorem ipsum dolor sit amet, consectetur :</strong> Ut enim ad</div>
    <div class="event-line">minima veniam, quis nostrum exercitationem ullam</div>
    <div class="event-meta">
      <svg width="14" height="20" viewBox="0 0 14 20"><path d="M7 0C3.1 0 0 3.1 0 7c0 5.2 7 13 7 13s7-7.8 7-13c0-3.9-3.1-7-7-7zm0 9.5A2.5 2.5 0 1 1 7 4.5a2.5 2.5 0 0 1 0 5z" fill="#111"/></svg>
      <span style="margin-left:10px">410 W. Harbor Street, Suite</span><span class="sep">|</span>
      <svg width="20" height="20" viewBox="0 0 20 20" fill="none" stroke="#d70c4e" stroke-width="1.4"><circle cx="10" cy="10" r="8.5"/><ellipse cx="10" cy="10" rx="3.8" ry="8.5"/><path d="M1.5 10h17M3 5.5h14M3 14.5h14"/></svg>
      <span class="event-link">www.northvale-events.com</span>
    </div>
  </div>
</div>

<!-- featured event cards -->
<article class="event-card" style="top:873px">
  <div class="card-top"><span class="card-name">Event 1</span><span class="card-date">June 02,2024</span></div>
  <p class="card-body">Lorem ipsum dolor sit amet, consectetur adipiscing elit, sed do eiusmod tempor incididunt ut labore et dolore magna aliqua.Ut enim ad minim veniam, quis nostrud exercitation ullamco laboris nisi ut aliquip ex ea commodo consequat.</p>
</article>
<article class="event-card" style="top:1215px">
  <div class="card-top"><span class="card-name">Event 2</span><span class="card-date">June 02,2024</span></div>
  <p class="card-body">Lorem ipsum dolor sit amet, consectetur adipiscing elit, sed do eiusmod tempor incididunt ut labore et dolore magna aliqua.Ut enim ad minim veniam, quis nostrud exercitation ullamco laboris nisi ut aliquip ex ea commodo consequat.</p>
</article>
<article class="event-card" style="top:1556px">
  <div class="card-top"><span class="card-name">Event 3</span><span class="card-date">June 02,2024</span></div>
  <p class="card-body">Lorem ipsum dolor sit amet, consectetur adipiscing elit, sed do eiusmod tempor incididunt ut labore et dolore magna aliqua.Ut enim ad minim veniam, quis nostrud exercitation ullamco laboris nisi ut aliquip ex ea commodo consequat.</p>
</article>

<!-- newsletter signup -->
<h2 class="section-title newsletter-title">Sign Up To <span class="accent">Our Newsletter</span></h2>
<p class="newsletter-copy">Lorem ipsum dolor sit amet, consectetur adipiscing elit, sed do eiusmod tempor incididunt ut labore et dolore magna aliqua.<br>Ut enim ad minim veniam, quis nostrud exercitation ullamco laboris nisi ut aliquip ex ea commodo consequat.</p>
<div class="email-input">Enter Email Address</div>
<a class="btn subscribe">Subscribe</a>

<footer class="site-footer">
  <span class="brand-name footer-brand">Northvale</span>
  <h3 class="contact-title">CONTACT&nbsp; DETAILS</h3>

  <div class="contact-item" style="left:397px;top:138px">
    <span class="icon-dot"><svg width="14" height="20" viewBox="0 0 14 20"><path d="M7 0C3.1 0 0 3.1 0 7c0 5.2 7 13 7 13s7-7.8 7-13c0-3.9-3.1-7-7-7zm0 9.5A2.5 2.5 0 1 1 7 4.5a2.5 2.5 0 0 1 0 5z" fill="#fff"/></svg></span>
    <span>410 W. Harbor Street, Suite<br>220 Lakeview, CA 90210</span>
  </div>
  <div class="contact-item" style="left:791px;top:157px">
    <span class="icon-dot"><svg width="22" height="22" viewBox="0 0 24 24"><path d="M6.6 10.8a15 15 0 0 0 6.6 6.6l2.2-2.2c.3-.3.7-.4 1-.2 1.1.4 2.3.6 3.6.6.6 0 1 .4 1 1V20c0 .6-.4 1-1 1A17 17 0 0 1 3 4c0-.6.4-1 1-1h3.5c.6 0 1 .4 1 1 0 1.3.2 2.5.6 3.6.1.3 0 .7-.2 1z" fill="#fff"/><path d="M15 3a6 6 0 0 1 6 6M15 6.5a2.5 2.5 0 0 1 2.5 2.5" stroke="#fff" stroke-width="1.6" fill="none"/></svg></span>
    <span>Fax: 05550123</span>
  </div>
  <div class="contact-item" style="left:397px;top:257px">
    <span class="icon-dot"><svg width="20" height="20" viewBox="0 0 24 24"><path d="M6.6 10.8a15 15 0 0 0 6.6 6.6l2.2-2.2c.3-.3.7-.4 1-.2 1.1.4 2.3.6 3.6.6.6 0 1 .4 1 1V20c0 .6-.4 1-1 1A17 17 0 0 1 3 4c0-.6.4-1 1-1h3.5c.6 0 1 .4 1 1 0 1.3.2 2.5.6 3.6.1.3 0 .7-.2 1z" fill="#fff"/></svg></span>
    <span>Phone: +1 555 0100 0199</span>
  </div>
  <div class="contact-item" style="left:791px;top:257px">
    <span class="icon-dot"><svg width="22" height="16" viewBox="0 0 22 16"><rect x="0" y="0" width="22" height="16" rx="2" fill="#fff"/><path d="M1 1.5l10 7 10-7" stroke="#d70c4e" stroke-width="1.8" fill="none"/></svg></span>
    <span>advisors@northvale-events.com</span>
  </div>

  <div class="footer-rule"></div>
  <p class="copyright">Copyrights@2024.northvale.All Rights Reserved</p>
</footer>

</body>
</html>
```